Hero Image Redesign for TRIL Consulting Website

About us:
TRIL Consulting is an organisational psychology and human resource management consulting firm based in Melbourne, Australia (www.trilconsult.com.au). We are a B2B offering a range of organisational psychology measurement and consulting. The largest part of our business is our online psychometric assessments, which are self-managed via an online portal, which is currently used by many organisations worldwide as part of their recruitment process.

What we are looking for:
We are seeking assistance to redesign an image located above the fold - on the top right hand side of homepage. We want an image of a small group of diverse people happily working together using a laptop (either individually or as a group), overlayed with graphic representations reflective of using our online Psychometric Assessment tool, in an interactive fashion.

The graphics will highlight key features of the self-service TRIL Psychometric Assessment Portal, specifically ease of use, flexibility and our integrated approach. We want the image to look clean, clear, minimal, with use of negative space. All graphics must be accessible (including sufficient colour contrast and text size).

We would like the graphic to feature 3 “pop ups” highlighting features, and these should appear over the image:

1. Setup participants easily online
2. Check the status of an assessment
3. View participants’ reports

Examples from other SaaS websites attached.

The final design should communicate trust, reliability, our scientific evidence based approach, and our approachable and friendly customer service.

Our main brand colours are:
• Navy – HEX #2F2971
• Mid Blue – HEX #0C75C0
• Black – HEX #000000

About TRIL’ website and potential for future work:

• TRIL’ website pages have been created using Bricks Builder for WordPress.
• There is a strong possibility of future projects following successful delivery. We are an excellent client – ethical, professional and with a genuine commitment to partnership.

Need extra days to review

```html
<!DOCTYPE html>
<html lang="en">
<head>
<meta charset="utf-8">
<title>TRIL Consulting – Hero Concepts</title>
<link rel="stylesheet" href="https://fonts.googleapis.com/css2?family=Poppins:wght@400;500;600&family=Lexend:wght@500;600&display=swap">
<style>
:root{
  --stage:#7e7e7e;
  --navy:#2f2971;
  --teal:#a7e2dc;
  --teal-line:#9fdcd4;
  --halo:#eef8f7;
  --nav-bg:#f6f6f6;
  --ink:#222;
  --body:#505055;
  --white:#fff;
}
*{box-sizing:border-box;margin:0;padding:0}
html,body{width:961px;height:1200px;overflow:hidden;background:var(--stage);font-family:"Poppins",sans-serif}
.screen{position:absolute;left:60px;width:841px;height:501px;background:var(--white);overflow:hidden;box-shadow:0 2px 8px rgba(0,0,0,.15)}
.screen--one{top:72px}
.screen--two{top:626px}
.topbar{height:28px;background:var(--navy);color:var(--white);font-size:8.6px;font-weight:500;display:flex;align-items:center;justify-content:center;gap:4px}
.topbar a{color:var(--teal);text-decoration:underline}
.navbar{height:46px;background:var(--nav-bg);display:flex;align-items:center;justify-content:space-between;padding:0 25px 0 26px}
.brand{display:flex;align-items:center;gap:6px;color:var(--navy);font-weight:600;font-size:15px;letter-spacing:.5px}
.brand-mark{width:14px;height:14px;background:var(--teal)}
.nav{display:flex;gap:19px;font-size:9px;color:var(--ink)}
.nav span.drop::after{content:"";display:inline-block;width:4px;height:4px;border-right:1.2px solid var(--ink);border-bottom:1.2px solid var(--ink);transform:rotate(45deg);margin:0 0 2px 6px}
.hero-title{position:absolute;left:47px;top:118px;font-family:"Lexend",sans-serif;font-weight:600;font-size:39px;line-height:48px;color:var(--navy)}
.hero-lede{position:absolute;left:47px;top:284px;width:400px;font-size:14px;line-height:27px;color:var(--body)}
.btn{position:absolute;top:376px;width:141px;height:37px;display:flex;align-items:center;justify-content:center;font-size:10.2px;font-weight:600;border-radius:2px;box-shadow:0 2px 4px rgba(0,0,0,.12)}
.btn--primary{left:47px;background:var(--navy);color:var(--white)}
.btn--secondary{left:213px;background:var(--teal);color:var(--navy)}
.photo{position:absolute;background:linear-gradient(135deg,#d9cfc4,#8c8d9a 45%,#4a5368 70%,#cfd4da)}
.photo--card{left:439px;top:150px;width:322px;height:260px;border:2px solid var(--teal-line);border-radius:18px}
.dot-field{position:absolute;left:709px;top:132px;width:70px;height:76px;background:#f7f7f9}
.popup{position:absolute;width:142px;height:59px;background:var(--white);border-radius:8px;font-size:12.3px;line-height:17.5px;color:var(--ink);padding:12px 0 0 17px}
.popup--outlined{border:2px solid var(--teal-line)}
.popup--shadow{box-shadow:0 2px 10px rgba(0,0,0,.12)}
.icon-badge{position:absolute;border-radius:50%;display:flex;align-items:center;justify-content:center}
.icon-badge--white{width:52px;height:52px;background:var(--white);box-shadow:0 2px 10px rgba(0,0,0,.12)}
.icon-badge--teal{background:var(--teal)}
.icon-badge--navy{background:var(--navy)}
.icon-badge--lg{width:60px;height:60px}
.icon-badge--md{width:52px;height:52px}
.halo{position:absolute;left:458px;top:114px;width:344px;height:344px;border-radius:50%;background:var(--halo)}
.photo--round{left:489px;top:145px;width:280px;height:280px;border-radius:50%}
.feature-label{position:absolute;font-size:12.3px;line-height:17.5px;color:var(--ink);white-space:nowrap}
.feature-label--right{text-align:right}
</style>
</head>
<body>

<svg width="0" height="0" style="position:absolute">
  <defs>
    <symbol id="ico-setup" viewBox="0 0 40 40">
      <rect x="6" y="12" width="24" height="17" rx="1.5" fill="none" stroke="currentColor" stroke-width="2.6"/>
      <rect x="3" y="29" width="30" height="3" rx="1" fill="currentColor"/>
      <circle cx="15" cy="18" r="3" fill="currentColor"/>
      <path d="M10 26c0-4 10-4 10 0z" fill="currentColor"/>
      <rect x="22" y="4" width="15" height="10" rx="2" fill="currentColor"/>
      <path d="M25 14l-2 4 5-4z" fill="currentColor"/>
      <circle cx="26" cy="9" r="1.2" fill="#fff"/><circle cx="29.5" cy="9" r="1.2" fill="#fff"/><circle cx="33" cy="9" r="1.2" fill="#fff"/>
    </symbol>
    <symbol id="ico-reports" viewBox="0 0 40 40">
      <rect x="5" y="22" width="5" height="13" fill="currentColor"/>
      <rect x="13" y="16" width="5" height="19" fill="currentColor"/>
      <rect x="21" y="20" width="5" height="15" fill="currentColor"/>
      <rect x="29" y="12" width="5" height="23" fill="currentColor"/>
      <polyline points="7,15 15,9 23,13 33,4" fill="none" stroke="currentColor" stroke-width="2"/>
      <circle cx="7" cy="15" r="2" fill="currentColor"/><circle cx="15" cy="9" r="2" fill="currentColor"/>
      <circle cx="23" cy="13" r="2" fill="currentColor"/><circle cx="33" cy="4" r="2" fill="currentColor"/>
    </symbol>
    <symbol id="ico-status" viewBox="0 0 40 40">
      <path d="M13 4h18l5 5v27H13z" fill="none" stroke="currentColor" stroke-width="2.4"/>
      <line x1="20" y1="12" x2="31" y2="12" stroke="currentColor" stroke-width="2"/>
      <line x1="24" y1="18" x2="31" y2="18" stroke="currentColor" stroke-width="2"/>
      <line x1="25" y1="24" x2="31" y2="24" stroke="currentColor" stroke-width="2"/>
      <line x1="18" y1="30" x2="31" y2="30" stroke="currentColor" stroke-width="2"/>
      <circle cx="14" cy="22" r="7" fill="#fff" stroke="currentColor" stroke-width="2.6"/>
      <line x1="9" y1="27" x2="3" y2="34" stroke="currentColor" stroke-width="3.4" stroke-linecap="round"/>
    </symbol>
  </defs>
</svg>

<!-- Concept A -->
<section class="screen screen--one">
  <div class="topbar">Register now for our <a>free virtual workshops</a> | TRIL Consulting Clients: <a>Login to the Portal</a></div>
  <header class="navbar">
    <div class="brand"><span class="brand-mark"></span>TRIL CONSULTING</div>
    <nav class="nav">
      <span class="drop">Psychometric testing</span><span class="drop">Employee wellbeing</span><span class="drop">HR consulting</span><span>Events</span><span class="drop">Knowledge hub</span><span class="drop">About us</span><span>Contact</span>
    </nav>
  </header>
  <h1 class="hero-title">Organisational<br>Psychology<br>Consulting</h1>
  <p class="hero-lede">Optimise your workforce with psychometric<br>testing, engagement surveys, wellbeing measures,<br>and organisational development.</p>
  <a class="btn btn--primary">Psychometric Testing</a>
  <a class="btn btn--secondary">Speak to an Expert &nbsp;→</a>

  <div class="dot-field" role="img" aria-label="Decorative dot grid"></div>
  <div class="photo photo--card" role="img" aria-label="Photo of a smiling, diverse team gathered around a laptop"></div>
  <div class="icon-badge icon-badge--white" style="left:370px;top:101px;color:var(--navy)"><svg width="30" height="30"><use href="#ico-setup"/></svg></div>
  <div class="popup popup--outlined" style="left:351px;top:168px">Setup participants<br>easily online</div>
  <div class="icon-badge icon-badge--white" style="left:773px;top:259px;color:var(--navy)"><svg width="30" height="30"><use href="#ico-reports"/></svg></div>
  <div class="popup popup--outlined" style="left:692px;top:323px">View participants’<br>reports</div>
  <div class="popup popup--shadow" style="left:390px;top:346px">Check the status<br>of an assessment</div>
  <div class="icon-badge icon-badge--teal icon-badge--md" style="left:396px;top:423px;color:var(--navy)"><svg width="30" height="30"><use href="#ico-status"/></svg></div>
</section>

<!-- Concept B -->
<section class="screen screen--two">
  <div class="topbar">Register now for our <a>free virtual workshops</a> | TRIL Consulting Clients: <a>Login to the Portal</a></div>
  <header class="navbar">
    <div class="brand"><span class="brand-mark"></span>TRIL CONSULTING</div>
    <nav class="nav">
      <span class="drop">Psychometric testing</span><span class="drop">Employee wellbeing</span><span class="drop">HR consulting</span><span>Events</span><span class="drop">Knowledge hub</span><span class="drop">About us</span><span>Contact</span>
    </nav>
  </header>
  <h1 class="hero-title">Organisational<br>Psychology<br>Consulting</h1>
  <p class="hero-lede">Optimise your workforce with psychometric<br>testing, engagement surveys, wellbeing measures,<br>and organisational development.</p>
  <a class="btn btn--primary">Psychometric Testing</a>
  <a class="btn btn--secondary">Speak to an Expert &nbsp;→</a>

  <div class="halo"></div>
  <div class="photo photo--round" role="img" aria-label="Photo of three colleagues laughing together over a laptop"></div>
  <p class="feature-label feature-label--right" style="right:120px;top:106px">View participants’<br>reports</p>
  <div class="icon-badge icon-badge--teal icon-badge--lg" style="left:731px;top:117px;color:var(--navy)"><svg width="34" height="34"><use href="#ico-reports"/></svg></div>
  <p class="feature-label feature-label--right" style="right:383px;top:182px">Setup participants<br>easily online</p>
  <div class="icon-badge icon-badge--navy icon-badge--lg" style="left:469px;top:175px;color:var(--white)"><svg width="34" height="34"><use href="#ico-setup"/></svg></div>
  <div class="icon-badge icon-badge--teal icon-badge--lg" style="left:579px;top:433px;color:var(--navy)"><svg width="34" height="34"><use href="#ico-status"/></svg></div>
  <p class="feature-label" style="left:655px;top:443px">Check the status of<br>an assessment</p>
</section>

</body>
</html>
```